Fairbrook's Vacation Rentals Business Card

Multi Million dollar villa rentals in the Dominican Republic.

Industry/Entity Type

Business

Contact Information for Business Card

I am looking for a high-end look around my company name/logo (see attached) on one side incorporating the following info: first and last name, title, address, phone #, email and company website. On the backside I want to add a full color picture of one of our villas (see attached).

```html
<!DOCTYPE html>
<html lang="en">
<head>
<meta charset="UTF-8">
<title>Fairbrook's Vacation Rentals – Business Card</title>
<link href="https://fonts.googleapis.com/css2?family=Montserrat:wght@400;500;800&display=swap" rel="stylesheet">
<style>
  :root {
    --bg: #ecebe8;
    --card-white: #ffffff;
    --ink: #1c1c1c;
    --band-dark: #232222;
    --accent-orange: #f26f21;
    --divider: #2a2a2a;
    --photo-light: #d8dcdf;
    --photo-deep: #8fb6d2;
  }
  * { margin: 0; padding: 0; box-sizing: border-box; }
  html, body { width: 1200px; height: 1000px; overflow: hidden; }
  body {
    background: var(--bg);
    display: flex;
    align-items: center;
    justify-content: center;
    gap: 40px;
  }
  .card {
    position: relative;
    width: 540px;
    height: 310px;
    border-radius: 24px;
    overflow: hidden;
    background: var(--card-white);
    box-shadow: 0 6px 20px rgba(0,0,0,0.18);
  }
  .card-front .swoosh { position: absolute; inset: 0; }
  .brand {
    position: absolute;
    left: 40px;
    top: 122px;
    display: flex;
    align-items: center;
    gap: 8px;
    font-family: 'Montserrat', sans-serif;
    font-weight: 500;
    color: var(--ink);
  }
  .brand-dot {
    width: 26px; height: 26px; border-radius: 50%;
    background: var(--accent-orange);
    flex: none;
  }
  .brand-name { line-height: 1.05; }
  .brand-name .primary { display: block; font-size: 21px; }
  .brand-name .secondary { display: block; font-size: 11px; letter-spacing: 1.2px; text-transform: uppercase; }
  .divider {
    position: absolute;
    left: 258px;
    top: 45px;
    width: 1.5px;
    height: 135px;
    background: var(--divider);
  }
  .contact {
    position: absolute;
    left: 284px;
    top: 40px;
    color: var(--ink);
    font-family: 'Montserrat', sans-serif;
    font-weight: 400;
  }
  .contact .person-name {
    font-weight: 800;
    font-size: 21px;
    letter-spacing: 0.3px;
    line-height: 1.2;
  }
  .contact .person-title {
    font-size: 13px;
    letter-spacing: 0.8px;
    margin-bottom: 12px;
  }
  .contact .lines { font-size: 12px; line-height: 1.4; }
  .contact .address { font-size: 12px; line-height: 1.4; margin-top: 6px; }
  .villa-photo {
    position: absolute; inset: 0;
    background: linear-gradient(180deg, var(--photo-light) 0%, var(--photo-deep) 100%);
  }
</style>
</head>
<body>
  <section class="card card-front">
    <svg class="swoosh" viewBox="0 0 540 310" width="540" height="310" aria-hidden="true">
      <path d="M0,200 Q250,250 540,150 L540,310 L0,310 Z" fill="var(--accent-orange)"/>
      <path d="M0,216 Q260,262 540,166 L540,310 L0,310 Z" fill="var(--band-dark)"/>
    </svg>
    <div class="brand">
      <span class="brand-dot"></span>
      <span class="brand-name">
        <span class="primary">Fairbrook's</span>
        <span class="secondary">Vacation Rentals</span>
      </span>
    </div>
    <div class="divider"></div>
    <div class="contact">
      <div class="person-name">JOHN DOE</div>
      <div class="person-title">MANAGER</div>
      <div class="lines">
        +12 123 456 7890<br>
        youremail@domain.com<br>
        www.yoursite.com
      </div>
      <div class="address">
        412 Harbor Lane<br>
        Eastbrook, PA 18099
      </div>
    </div>
  </section>

  <section class="card card-back">
    <div class="villa-photo" role="img" aria-label="Full-colour photograph of a luxury villa with a pool"></div>
  </section>
</body>
</html>
```